Retirement planning flyer

We need a flyer to market to people who are seeking advice on retirement planning. I will attach some images/articles for ideas. We prefer a graphic centric layout rather than a super wordy design. Please include my name Brent Halvorick and my contact info phone 561-847-2605 and website halvorickinsurance.example somewhere on the flyer. I have also attached our company logo.

```html
<!DOCTYPE html>
<html lang="en">
<head>
<meta charset="utf-8">
<title>Retirement Planning Flyers – Halvorick Insurance</title>
<link rel="stylesheet" href="https://fonts.googleapis.com/css2?family=Oswald:wght@400;500;600&family=Arimo:ital,wght@0,400;0,700;1,400;1,700&display=swap">
<style>
  :root {
    --teal: #2d8497;
    --teal-deep: #1f6f82;
    --ink: #2b2b2b;
    --grey: #555;
    --sand: #fbd58d;
    --sand-light: #fde3b0;
    --wave: #f6b774;
    --wave-light: #fbd2a3;
    --paper: #ffffff;
    --stage: #ffffff;
  }
  * { box-sizing: border-box; margin: 0; padding: 0; }
  html, body { width: 1200px; height: 876px; overflow: hidden; background: var(--stage); }
  body { position: relative; font-family: "Arimo", Arial, sans-serif; color: var(--ink); }

  .flyer {
    position: absolute;
    width: 560px;
    height: 786px;
    background: var(--paper);
    overflow: hidden;
    box-shadow: 0 2px 8px rgba(0,0,0,.25);
  }
  .flyer--plan { left: 27px; top: 29px; }
  .flyer--rollover { left: 612px; top: 62px; }

  .abs { position: absolute; }
  .condensed { font-family: "Oswald", "Arial Narrow", sans-serif; }

  /* Shared bands */
  .band-sand { position: absolute; left: 0; right: 0; background: var(--sand); }
  .wave-band { position: absolute; left: 0; width: 560px; }

  .cta-strip { position: absolute; left: 0; right: 0; background: var(--paper); text-align: center; }
  .cta-strip__title { font-family: "Oswald", sans-serif; font-weight: 500; color: var(--teal); font-size: 25px; line-height: 1.2; padding-top: 6px; }
  .cta-strip__sub { font-family: "Oswald", sans-serif; font-weight: 500; font-size: 15.5px; color: var(--ink); margin-top: 4px; }

  .brand { position: absolute; display: flex; align-items: center; gap: 10px; }
  .brand__name { font-family: "Oswald", sans-serif; font-weight: 400; font-size: 40px; color: var(--ink); letter-spacing: 1px; line-height: 1; }
  .brand__mark { width: 30px; height: 30px; border-radius: 50%; background: var(--teal); flex: none; }

  .contact { position: absolute; text-align: left; }
  .contact__name { font-style: italic; font-weight: 700; font-size: 22px; color: var(--ink); }
  .contact__phone { font-weight: 700; font-size: 24px; color: var(--teal); letter-spacing: 1.5px; margin-top: 6px; }

  .website { position: absolute; left: 0; right: 0; text-align: center; font-weight: 700; font-size: 19px; color: var(--ink); letter-spacing: .3px; }
  .website__domain { color: var(--teal); }

  /* Plan flyer */
  .plan-photo {
    position: absolute; left: 0; top: 0; width: 560px; height: 345px;
    background: linear-gradient(135deg, #e8eef2 0%, #f4f1ea 40%, #ece3d6 70%, #dfe6dc 100%);
  }
  .plan-headline { position: absolute; left: 30px; color: var(--teal); font-weight: 500; font-size: 22.5px; line-height: 1.3; letter-spacing: .2px; }
  .free-offer { position: absolute; left: 36px; top: 400px; width: 148px; text-align: center; color: var(--teal); }
  .free-offer__kicker { font-size: 9.5px; letter-spacing: 5px; color: var(--grey); border-top: 1.5px solid var(--teal); padding-top: 3px; }
  .free-offer__word { font-weight: 700; font-size: 58px; line-height: 1; letter-spacing: -1px; margin: 2px 0; }
  .free-offer__foot { font-size: 9.5px; letter-spacing: 5px; color: var(--grey); border-bottom: 1.5px solid var(--teal); padding-bottom: 3px; }

  .service-list { position: absolute; list-style: none; font-family: "Oswald", sans-serif; font-size: 13px; line-height: 18.5px; color: var(--ink); }
  .service-list li { padding-left: 14px; text-indent: -14px; }
  .service-list li::before { content: "✓ "; }

  /* Rollover flyer */
  .rollover-headline { position: absolute; left: 0; right: 0; top: 30px; text-align: center; font-family: "Oswald", sans-serif; font-weight: 600; font-size: 29px; color: var(--teal); letter-spacing: .2px; }
  .rollover-tagline { position: absolute; left: 0; right: 0; top: 82px; text-align: center; font-style: italic; font-size: 20px; color: var(--grey); letter-spacing: .3px; }
  .rollover-photo {
    position: absolute; left: 100px; top: 112px; width: 360px; height: 148px;
    background: radial-gradient(ellipse at center, #f1e7dd 0%, #e6d5c4 45%, #f7f3ee 75%, #ffffff 100%);
  }
  .rollover-kicker { position: absolute; left: 0; right: 0; top: 268px; text-align: center; font-size: 22px; letter-spacing: 5px; color: var(--ink); }
  .rollover-benefit { position: absolute; left: 0; right: 0; top: 298px; text-align: center; font-family: "Oswald", sans-serif; font-weight: 500; font-size: 21px; color: var(--teal); }
  .rollover-question { position: absolute; left: 0; right: 0; top: 364px; text-align: center; font-family: "Oswald", sans-serif; font-weight: 600; font-size: 25px; color: var(--teal); }
  .rollover-promise { position: absolute; left: 0; right: 0; top: 396px; text-align: center; font-family: "Oswald", sans-serif; font-weight: 600; font-size: 25px; color: var(--ink); }
  .rollover-body { position: absolute; left: 40px; right: 40px; top: 440px; text-align: center; font-style: italic; font-size: 17px; line-height: 22px; color: var(--grey); }
</style>
</head>
<body>

<!-- Flyer 1: Plan for your financial future -->
<section class="flyer flyer--plan">
  <div class="plan-photo" role="img" aria-label="Photo of a smiling retired couple at a laptop in a bright room"></div>
  <div class="plan-headline condensed" style="top:44px;">PLAN FOR YOUR<br>FINANCIAL FUTURE.</div>
  <div class="plan-headline condensed" style="top:111px;">TAKE CONTROL OF YOUR<br>RETIREMENT ACCOUNTS.</div>

  <div class="band-sand" style="top:370px;height:152px;"></div>
  <svg class="wave-band" style="top:318px;" width="560" height="80" viewBox="0 0 560 80" aria-hidden="true">
    <path d="M0 30 C120 0 220 50 330 25 S500 5 560 22 L560 80 L0 80 Z" fill="var(--wave-light)"/>
    <path d="M0 45 C110 25 230 65 340 42 S490 28 560 40 L560 80 L0 80 Z" fill="var(--wave)"/>
    <path d="M0 62 C130 48 240 78 360 60 S500 52 560 58 L560 80 L0 80 Z" fill="var(--sand)"/>
  </svg>

  <div class="free-offer">
    <div class="free-offer__kicker">SCHEDULE YOUR</div>
    <div class="free-offer__word">FREE</div>
    <div class="free-offer__foot">CONSULTATION</div>
  </div>

  <ul class="service-list" style="left:213px;top:396px;width:160px;">
    <li>Getting started</li>
    <li>401(k)s &amp; company plans</li>
    <li>Investing</li>
    <li>Annuities IRAs</li>
    <li>Self-employment plans</li>
  </ul>
  <ul class="service-list" style="left:381px;top:396px;width:160px;">
    <li>Pensions and benefit plans</li>
    <li>Social Security</li>
    <li>Insurance</li>
    <li>Estate planning</li>
    <li>Living in retirement</li>
  </ul>

  <div class="cta-strip" style="top:522px;height:68px;">
    <div class="cta-strip__title">Call today for more information</div>
    <div class="cta-strip__sub">We can help you define, plan, and achieve your financial goals!</div>
  </div>

  <div class="band-sand" style="top:590px;height:196px;"></div>
  <div class="brand" style="left:26px;top:635px;">
    <span class="brand__name">HALVORICK</span>
    <span class="brand__mark"></span>
  </div>
  <div class="contact" style="left:355px;top:632px;">
    <div class="contact__name">Brent Halvorick</div>
    <div class="contact__phone">561-847-2605</div>
  </div>
  <div class="website" style="top:735px;">WWW.<span class="website__domain">HALVORICKINSURANCE</span>.EXAMPLE</div>
</section>

<!-- Flyer 2: Rollover your 401(k) -->
<section class="flyer flyer--rollover">
  <h1 class="rollover-headline">YOU’VE WORKED HARD FOR YOUR MONEY.</h1>
  <p class="rollover-tagline">Now it’s time your money works hard for you.</p>
  <div class="rollover-photo" role="img" aria-label="Photo of a relaxed bulldog lying on its back between two nest eggs labelled 401K and IRA"></div>
  <p class="rollover-kicker">ROLLOVER YOUR 401(k)</p>
  <p class="rollover-benefit">Take advantage of the universe of investment options.</p>

  <div class="band-sand" style="top:360px;height:176px;"></div>
  <svg class="wave-band" style="top:318px;" width="560" height="60" viewBox="0 0 560 60" aria-hidden="true">
    <path d="M0 22 C120 0 220 38 330 18 S500 2 560 16 L560 60 L0 60 Z" fill="var(--wave-light)"/>
    <path d="M0 34 C110 18 230 50 340 30 S490 20 560 30 L560 60 L0 60 Z" fill="var(--wave)"/>
    <path d="M0 46 C130 36 240 58 360 44 S500 38 560 42 L560 60 L0 60 Z" fill="var(--sand)"/>
  </svg>

  <h2 class="rollover-question">RETIRING OR CHANGING JOBS?</h2>
  <h2 class="rollover-promise">WE MAKE IT EASY TO ROLL OVER YOUR 401(k).</h2>
  <p class="rollover-body">What you do with these assets could significantly impact your lifestyle in retirement. Your future is too important to risk making the wrong decision. We can help — every step of the way.</p>

  <div class="cta-strip" style="top:536px;height:68px;">
    <div class="cta-strip__title">Call today for more information</div>
    <div class="cta-strip__sub">We can help you define, plan, and achieve your financial goals!</div>
  </div>

  <div class="band-sand" style="top:604px;height:182px;"></div>
  <div class="brand" style="left:30px;top:645px;">
    <span class="brand__name">HALVORICK</span>
    <span class="brand__mark"></span>
  </div>
  <div class="contact" style="left:355px;top:642px;">
    <div class="contact__name">Brent Halvorick</div>
    <div class="contact__phone">561-847-2605</div>
  </div>
  <div class="website" style="top:742px;">WWW.<span class="website__domain">HALVORICKINSURANCE</span>.EXAMPLE</div>
</section>

</body>
</html>
```